2022 American Football Calendar Design

This project is for an American High School Football calendar for 2022.

The theme is US football and specifically high-school football for a streaming TV show about American high-school football.

The total number of pages will be 28 with the cover being 4 pages and the months being the other 24 pages.

Design Elements:

1. Each month will have 2 pages. 1 for the lead / hero image and one for the days of the month.

2. We will supply the images for each month of the calendar. There may be multiple potential image options for a given month. You can, as the designer, choose to use one or multiple images for the month if you feel the design would benefit.

3. Each month will have special days including US Holidays and special Football Days. We will supply a spreadsheet with all of these days and dates.

4. The boxes for the days should be square with enough space to allow for writing in the box when the calendar is printed.

5. Each month will also have a special quote text area that will contain special informational or an inspirational quote.

6. The calendar dimensions are 11" x 8 1/2" (US Letter - landscape orientation) - folded. So each page is US Letter size. A print guide template is attached from the printing company.

7. The title of the calendar is Pine Summit 2022 Calendar.

For this contest please supply design concepts for the following:
1. Cover page;
2. Inside page;
3. Month Hero page;
4. Days of the month page;
5. Back cover page;

We will use these design concepts to choose the winner who will then need to finish the complete calendar design and preparation for printing.

Final Deliverables:

A. Complete 28 page calendar design - the winner will complete the design and layout of all pages.

B. Final print ready PDF at least 350 dpi with bleed for printing. Please see the attached size template from the printing company with guides.

C. Layered & Fully Editable Source File - InDesign, AI or PSD (NO COREL DRAW PLEASE - Adobe products only please). If vector files are supplied, we will also need a text editable version.

D. Any fonts used - we have licensing, if needed, available from Lumeth Type and Quorvix Assets.

We are looking for a fast turnaround on this project so it can be sent to the printer next week.

Target Market(s)

High-school football players and their family & friends

Industry/Entity Type

American football

Font styles to use
Other font styles liked:
• Collegiate type sports fonts.

Colors

Designer to choose colors to be used in the design.

Requirements
Must have
• 350 DPI print-ready PDF, Fully editable source files including fonts & layers (NO Corel Draw) - see brief
Nice to have
• vector (AI) and PSD
Should not have
• Do not use Corel Draw

```html
<!DOCTYPE html>
<html lang="en">
<head>
<meta charset="utf-8">
<title>Pine Summit 2022 Calendar – Design Concepts</title>
<link rel="stylesheet" href="https://fonts.googleapis.com/css2?family=Titillium+Web:wght@600;700;900&family=Open+Sans:ital,wght@0,400;0,600;0,700;1,600&display=swap">
<style>
  :root{
    --stage:#d3d4d6;
    --paper:#ffffff;
    --olive:#8a8540;
    --olive-dark:#6e6a2c;
    --olive-light:#c9c68a;
    --olive-pale:#f2f1df;
    --purple:#4c4a7a;
    --purple-light:#a9a8cf;
    --purple-pale:#e9e8f3;
    --pink:#e5337c;
    --pink-pale:#f7dbe7;
    --gold-1:#fff6a8;
    --gold-2:#d9b83a;
    --ink:#1f1f24;
    --grid-line:#cfcb9a;
    --spiral:#6b6b70;
  }
  *{box-sizing:border-box;margin:0;padding:0}
  html,body{width:1200px;height:791px;overflow:hidden}
  body{background:var(--stage);position:relative;font-family:"Open Sans",Arial,sans-serif;color:var(--ink)}

  .page{position:absolute;background:var(--paper);overflow:hidden;box-shadow:0 4px 10px rgba(0,0,0,.25)}
  .page::before{content:"";position:absolute;left:6px;right:6px;top:2px;height:3px;border-top:3px dotted var(--spiral);z-index:5}
  .photo{position:absolute;inset:0}
  .swoosh{position:absolute;inset:0;width:100%;height:100%}

  /* Covers */
  .cover{width:322px;height:246px}
  .cover--front{left:58px;top:86px}
  .cover--back{left:28px;top:382px}
  .cover--front .photo{background:radial-gradient(ellipse at 45% 70%,#4a5a6a 0%,#25303a 40%,#0b0d10 75%)}
  .cover--back .photo{background:radial-gradient(ellipse at 40% 40%,#3a1416 0%,#1a0c18 45%,#0a0812 80%)}
  .cover-title{position:absolute;text-align:right;font-family:"Titillium Web",Arial,sans-serif;line-height:.9}
  .cover--front .cover-title{right:14px;top:14px}
  .cover--back .cover-title{right:18px;top:170px}
  .cover-brand{font-weight:700;font-size:14px;display:block}
  .cover--front .cover-brand{color:#d9d34a}
  .cover--back .cover-brand{color:#fff;font-size:11px}
  .cover-year{display:block;font-weight:900;font-size:44px;letter-spacing:-2px;background:linear-gradient(180deg,var(--gold-1),var(--gold-2) 70%,#8f7a1e);-webkit-background-clip:text;background-clip:text;color:transparent}
  .cover--back .cover-year{font-size:32px}
  .cover-word{display:block;font-weight:700;font-size:17px;color:#fff;letter-spacing:.5px}
  .cover--back .cover-word{font-size:12px}

  /* Month spreads */
  .spread{position:absolute}
  .spread--jan{left:497px;top:22px;width:312px;height:456px;--accent:var(--olive);--accent-dark:var(--olive-dark);--accent-light:var(--olive-light);--accent-pale:var(--olive-pale)}
  .spread--feb{left:824px;top:306px;width:334px;height:452px;--accent:var(--purple);--accent-dark:var(--purple);--accent-light:var(--purple-light);--accent-pale:var(--purple-pale);--grid-line:#c9c8e0}
  .hero-page{position:absolute;left:0;top:0;width:100%;height:50%}
  .spread--jan .hero-page .photo{background:linear-gradient(160deg,#6e6b2c,#55582a 55%,#3f4522)}
  .spread--feb .hero-page .photo{background:linear-gradient(160deg,#b9b3c8,#8b7f74 50%,#2d3045)}
  .days-page{position:absolute;left:0;bottom:0;width:100%;height:50%}

  .year-tag{position:absolute;left:6px;top:26px;width:84px;height:22px;background:var(--accent-dark);color:#fff;font-family:"Titillium Web",Arial,sans-serif;font-weight:700;font-size:17px;line-height:22px;padding-left:18px;clip-path:polygon(0 0,82% 0,100% 100%,0 100%);z-index:2}
  .month-title{position:absolute;right:14px;top:12px;display:flex;align-items:center;gap:6px;font-family:"Titillium Web",Arial,sans-serif;font-weight:700;color:var(--accent);font-size:21px;z-index:2}
  .month-num{background:var(--accent-dark);color:#fff;font-size:16px;padding:0 6px;line-height:20px}

  .quote{position:absolute;left:6px;top:54px;width:54px;height:100px;background:linear-gradient(180deg,var(--accent-pale),#fff);border-radius:4px;font-style:italic;font-weight:600;font-size:7.2px;line-height:13px;text-align:center;color:var(--accent);padding-top:18px}
  .quote-mark{position:absolute;font-size:16px;font-weight:700;font-style:normal;color:var(--accent)}
  .quote-mark--open{left:4px;top:-2px}
  .quote-mark--close{right:4px;bottom:-2px}
  .notes{position:absolute;left:6px;top:158px;width:54px}
  .notes-label{font-size:5.5px;font-weight:700;text-align:center;font-style:italic;margin-bottom:3px}
  .notes-line{height:10px;border-bottom:1px solid #d6d6d6}

  .month-grid{position:absolute;left:62px;top:50px;width:242px;display:grid;grid-template-columns:repeat(7,1fr);grid-auto-rows:24px;font-family:"Titillium Web",Arial,sans-serif;font-weight:700;font-size:10px;border-left:1px solid var(--grid-line);z-index:2}
  .month-grid .dow{height:16px;line-height:16px;text-align:center;font-size:9px;border-right:1px solid var(--grid-line)}
  .month-grid .dow--sun{background:var(--pink);color:#fff}
  .month-grid .day{text-align:center;padding-top:3px;border-right:1px solid var(--grid-line);border-bottom:1px solid var(--grid-line)}
  .month-grid .day--sun{background:var(--pink-pale);color:var(--pink)}
  .spread--feb .month-grid{left:64px;top:54px;width:260px;grid-auto-rows:25px;font-size:10.5px}
  .spread--feb .quote{top:56px;width:56px}
  .spread--feb .notes{top:162px;width:56px}

  .fine-print{position:absolute;left:8px;bottom:12px;font-size:3.6px;color:#555;z-index:3}

  /* Yearly planner */
  .planner{left:390px;top:510px;width:314px;height:242px;background:linear-gradient(180deg,#f3e6ee,#fff 30%,#fff 80%,#eadbe6)}
  .planner-head{position:absolute;left:0;right:0;top:16px;text-align:center;font-family:"Titillium Web",Arial,sans-serif;line-height:.9}
  .planner-year{display:block;font-weight:900;font-size:30px;letter-spacing:-1px;background:linear-gradient(180deg,#f27fb0,var(--pink));-webkit-background-clip:text;background-clip:text;color:transparent}
  .planner-label{display:block;font-weight:700;font-size:8px;color:var(--pink)}
  .planner-grid{position:absolute;left:12px;right:10px;top:58px;display:grid;grid-template-columns:repeat(4,1fr);gap:6px 4px}
  .planner-month{height:54px;border:1px solid var(--pink);background:repeating-linear-gradient(180deg,#fff 0 7px,#d8d8d8 7px 8px);background-position:0 10px;background-color:#fff}
  .planner-month h3{font-size:4.5px;font-weight:700;color:var(--pink);text-align:center;background:#fff;height:9px;line-height:9px}
  .planner-month--jan{border-color:var(--olive)}
  .planner-month--jan h3{color:var(--olive-dark)}
  .planner-month--feb{border-color:var(--purple)}
  .planner-month--feb h3{color:var(--purple)}
</style>
</head>
<body>

<!-- Front cover -->
<section class="page cover cover--front">
  <div class="photo" role="img" aria-label="Night game action photo of a ball carrier running with teammates across the field"></div>
  <svg class="swoosh" viewBox="0 0 322 246" preserveAspectRatio="none" aria-hidden="true">
    <path d="M0 0H322V170C300 90 200 40 60 50C30 52 10 56 0 60Z" fill="#6f7344"/>
    <path d="M0 50C80 20 240 30 322 150V120C250 40 120 10 0 30Z" fill="#a7ad6b" opacity=".8"/>
    <path d="M0 62C100 40 230 60 322 170V160C240 70 110 45 0 56Z" fill="#d8d9a6" opacity=".7"/>
    <path d="M0 200C80 240 200 246 322 230V246H0Z" fill="#cfc98a" opacity=".6"/>
  </svg>
  <h1 class="cover-title">
    <span class="cover-brand">Pine Summit</span>
    <span class="cover-year">2022</span>
    <span class="cover-word">CALENDER</span>
  </h1>
</section>

<!-- Back cover -->
<section class="page cover cover--back">
  <div class="photo" role="img" aria-label="Dramatic low-light portrait of a player adjusting a football helmet"></div>
  <svg class="swoosh" viewBox="0 0 322 246" preserveAspectRatio="none" aria-hidden="true">
    <path d="M150 0C230 10 300 50 322 110V0Z" fill="#4b4fb0" opacity=".7"/>
    <path d="M180 0C250 20 310 70 322 140V120C300 60 250 20 200 0Z" fill="#7b7fe0" opacity=".6"/>
    <path d="M0 150C40 210 150 235 322 230V246H0Z" fill="#3b3f98" opacity=".8"/>
    <path d="M0 175C60 225 170 240 322 238V246H0Z" fill="#9a6fd8" opacity=".6"/>
  </svg>
  <h2 class="cover-title">
    <span class="cover-brand">Pine Summit</span>
    <span class="cover-year">2022</span>
    <span class="cover-word">CALENDER</span>
  </h2>
</section>

<!-- January spread -->
<section class="spread spread--jan">
  <div class="page hero-page">
    <div class="photo" role="img" aria-label="Aerial photo of a player standing in the painted end zone of the stadium field"></div>
    <svg class="swoosh" viewBox="0 0 312 228" preserveAspectRatio="none" aria-hidden="true">
      <path d="M240 0C280 10 305 25 312 40V0Z" fill="#d9d6a0" opacity=".8"/>
      <path d="M0 200C100 230 220 232 312 200V228H0Z" fill="#c7c480" opacity=".7"/>
    </svg>
  </div>
  <div class="page days-page">
    <svg class="swoosh" viewBox="0 0 312 228" preserveAspectRatio="none" aria-hidden="true">
      <path d="M0 0H312V14C200 30 80 22 0 8Z" fill="#d4d19a" opacity=".7"/>
      <path d="M0 228H312V170C250 210 120 222 0 216Z" fill="var(--olive-light)" opacity=".8"/>
      <path d="M0 228H312V196C220 224 100 228 0 224Z" fill="var(--olive)" opacity=".6"/>
    </svg>
    <div class="year-tag">2022</div>
    <h2 class="month-title">JANUARY <span class="month-num">01</span></h2>
    <aside class="quote">
      <span class="quote-mark quote-mark--open">&ldquo;</span>
      Don't<br>wait for<br>opportunity,<br>Create it
      <span class="quote-mark quote-mark--close">&rdquo;</span>
    </aside>
    <div class="notes">
      <p class="notes-label">Note</p>
      <div class="notes-line"></div><div class="notes-line"></div><div class="notes-line"></div><div class="notes-line"></div>
    </div>
    <div class="month-grid">
      <div class="dow dow--sun">SUN</div><div class="dow">MON</div><div class="dow">TUE</div><div class="dow">WED</div><div class="dow">THU</div><div class="dow">FRI</div><div class="dow">SAT</div>
      <div class="day day--sun"></div><div class="day"></div><div class="day"></div><div class="day"></div><div class="day"></div><div class="day"></div><div class="day">1</div>
      <div class="day day--sun">2</div><div class="day">3</div><div class="day">4</div><div class="day">5</div><div class="day">6</div><div class="day">7</div><div class="day">8</div>
      <div class="day day--sun">9</div><div class="day">10</div><div class="day">11</div><div class="day">12</div><div class="day">13</div><div class="day">14</div><div class="day">15</div>
      <div class="day day--sun">16</div><div class="day">17</div><div class="day">18</div><div class="day">19</div><div class="day">20</div><div class="day">21</div><div class="day">22</div>
      <div class="day day--sun">23</div><div class="day">24</div><div class="day">25</div><div class="day">26</div><div class="day">27</div><div class="day">28</div><div class="day">29</div>
      <div class="day day--sun">30</div><div class="day">31</div><div class="day"></div><div class="day"></div><div class="day"></div><div class="day"></div><div class="day"></div>
    </div>
    <p class="fine-print">*Game days and holidays noted here</p>
  </div>
</section>

<!-- Yearly planner -->
<section class="page planner">
  <svg class="swoosh" viewBox="0 0 314 242" preserveAspectRatio="none" aria-hidden="true">
    <path d="M0 0H314V30C220 10 100 20 0 50Z" fill="#e8cfe0" opacity=".7"/>
    <path d="M0 242H314V210C220 236 100 236 0 222Z" fill="#d7bfd3" opacity=".7"/>
  </svg>
  <h2 class="planner-head">
    <span class="planner-year">2022</span>
    <span class="planner-label">YEARLY PLANNER</span>
  </h2>
  <div class="planner-grid">
    <div class="planner-month planner-month--jan"><h3>January</h3></div>
    <div class="planner-month planner-month--feb"><h3>February</h3></div>
    <div class="planner-month"><h3>March</h3></div>
    <div class="planner-month"><h3>April</h3></div>
    <div class="planner-month"><h3>May</h3></div>
    <div class="planner-month"><h3>June</h3></div>
    <div class="planner-month"><h3>July</h3></div>
    <div class="planner-month"><h3>August</h3></div>
    <div class="planner-month"><h3>September</h3></div>
    <div class="planner-month"><h3>October</h3></div>
    <div class="planner-month"><h3>November</h3></div>
    <div class="planner-month"><h3>December</h3></div>
  </div>
</section>

<!-- February spread -->
<section class="spread spread--feb">
  <div class="page hero-page">
    <div class="photo" role="img" aria-label="Photo of a coach and a player talking while seated on rocks outdoors at sunset"></div>
    <svg class="swoosh" viewBox="0 0 334 226" preserveAspectRatio="none" aria-hidden="true">
      <path d="M260 0C300 12 325 28 334 45V0Z" fill="#d8d7ec" opacity=".8"/>
      <path d="M0 200C110 228 230 230 334 196V226H0Z" fill="var(--purple-light)" opacity=".7"/>
    </svg>
  </div>
  <div class="page days-page">
    <svg class="swoosh" viewBox="0 0 334 226" preserveAspectRatio="none" aria-hidden="true">
      <path d="M0 0H334V14C210 30 90 22 0 8Z" fill="#d9d8ec" opacity=".8"/>
      <path d="M0 226H334V168C260 208 130 220 0 214Z" fill="var(--purple-light)" opacity=".7"/>
      <path d="M0 226H334V194C230 222 110 226 0 222Z" fill="var(--purple)" opacity=".55"/>
    </svg>
    <div class="year-tag">2022</div>
    <h2 class="month-title">FEBRUARY <span class="month-num">02</span></h2>
    <aside class="quote">
      <span class="quote-mark quote-mark--open">&ldquo;</span>
      Don't<br>wait for<br>opportunity,<br>Create it
      <span class="quote-mark quote-mark--close">&rdquo;</span>
    </aside>
    <div class="notes">
      <div class="notes-line"></div><div class="notes-line"></div><div class="notes-line"></div><div class="notes-line"></div>
    </div>
    <div class="month-grid">
      <div class="dow dow--sun">SUN</div><div class="dow">MON</div><div class="dow">TUE</div><div class="dow">WED</div><div class="dow">THU</div><div class="dow">FRI</div><div class="dow">SAT</div>
      <div class="day day--sun"></div><div class="day"></div><div class="day">1</div><div class="day">2</div><div class="day">3</div><div class="day">4</div><div class="day">5</div>
      <div class="day day--sun">6</div><div class="day">7</div><div class="day">8</div><div class="day">9</div><div class="day">10</div><div class="day">11</div><div class="day">12</div>
      <div class="day day--sun">13</div><div class="day">14</div><div class="day">15</div><div class="day">16</div><div class="day">17</div><div class="day">18</div><div class="day">19</div>
      <div class="day day--sun">20</div><div class="day">21</div><div class="day">22</div><div class="day">23</div><div class="day">24</div><div class="day">25</div><div class="day">26</div>
      <div class="day day--sun">27</div><div class="day">28</div><div class="day"></div><div class="day"></div><div class="day"></div><div class="day"></div><div class="day"></div>
      <div class="day day--sun"></div><div class="day"></div><div class="day"></div><div class="day"></div><div class="day"></div><div class="day"></div><div class="day"></div>
    </div>
    <p class="fine-print">*Game days and holidays noted here</p>
  </div>
</section>

</body>
</html>
```